website redesign / Software / tech business

Task Description: Website Redesign for Tormique
Project Overview:

Redesign the Tormique website to enhance user experience and visual appeal while maintaining brand identity.

Incorporate existing header and footer elements with minor adjustments for improved functionality.

Introduce new sections highlighting the benefits of using Tormique's services.

Redesign the blog/news area and the "How It Works" section to improve usability and visual appeal.

Ensure the design communicates that Tormique is a modern, innovative software company in the insurance industry.

Update the font style to align with the design aesthetic of brindlequay.example.

Specific Requirements:

Header and Footer:

Ensure consistency with current design elements.

​A​gain header and footer to look like brindlequay.example

Enhance navigation for a seamless user experience.

Incorporate provided draft images for the header and footer for inspiration.

Existing Elements:

Review and refine existing content for clarity and relevance.

Update graphics and icons as needed to align with the new design theme.

New Elements Section: Benefits of Using Tormique: Create a dedicated section showcasing key benefits such as:

a. Competitive pricing through auction-based live quotes

Experience dynamic pricing based on real-time bidding from insurers, ensuring you get the best possible rates for your insurance.

b. Tailored insurance solutions for niche products

Tormique offers specialised coverage options designed for niche markets, including motor trade fleet insurance and more, with flexibility to suit unique business needs.

c. Streamlined process with direct interaction with insurers

No need for middlemen—connect directly with insurers for faster, more transparent quotes and coverage options.

d. No more calls from multiple brokers; all quotes provided online

Say goodbye to endless calls from brokers. All your quotes are provided online in one place, simplifying the process and saving you time.

e. The UK's first and only online digital service for niche products

Tormique is pioneering the market with an innovative, fully digital platform specifically designed for niche insurance products.

f. Artificial intelligence integrated to help you speed up the process of receiving quotes

Leverage cutting-edge AI technology to quickly analyse your needs and present relevant quotes, speeding up the entire process of obtaining insurance.

g. Purchase your policy within the live auction and speak to the provider directly, or let the auction run until the end to speak to your chosen provider

Gain full control over your insurance process by either engaging directly with the insurer during the live auction or waiting for the auction to end to select your ideal provider.

Redesign Blog/News Area:

Create a modern, clean, and user-friendly layout for the blog/news section.

Implement an easy-to-navigate format for articles and news updates.

Optimise for both desktop and mobile devices.

Include categorisation and filtering options for better content discovery.

Redesign “How It Works” Section:

Visual redesign of the existing "How It Works" steps.

Present the four steps in a user-friendly manner, possibly by placing them into a phone graphic or another creative visual representation.

Ensure clear, easy-to-understand icons or graphics that align with the overall website style.

Provide graphic design elements to visually enhance this section and make it more engaging.

Products Section:

Redesign the products section to accommodate both live products and coming soon products.

Display live products with relevant details, and indicate upcoming products with a "Coming Soon" label or section.

Allow easy expansion of this section as new products are introduced, with a flexible structure for future growth.

Design should be visually appealing and user-friendly, with clear calls to action for each product.

Additional Sections to Enhance Homepage:

Customer Testimonials & Success Stories:
Showcase real feedback and case studies from satisfied customers to build trust and credibility. This section should be visually distinct with short, punchy quotes and success stories.

Modern Software Features Overview:
Highlight Tormique as a cutting-edge software company with an emphasis on innovation, such as the integration of AI, user-friendly interfaces, and secure technology. This could include interactive features or a carousel of screenshots from the platform.

Call-to-Action (CTA) Buttons and Lead Generation:
Place clear CTAs such as "Get Started", "Request a Quote", throughout the page to guide users to take the next steps.

Interactive Demo or Video:
Add an interactive demo or a short explainer video that shows how Tormique works, offering a glimpse into the platform's user interface and its advantages.

About Us / Company Vision Section:
Provide a clear, modern, and brief description of Tormique's mission and values, focusing on innovation and commitment to revolutionising the insurance market.

Design Guidelines:

Maintain Tormique's brand colours (green predominant) and style guidelines.

Change the font to match the design aesthetic of brindlequay.example, ensuring it has a modern, clean, and professional feel.

- Additional Pages for Tormique Website:
Contact Us Page:

A user-friendly contact page for inquiries, customer support, or general questions.

Include a contact form with fields for name, email, phone number, and message.

Display company contact details such as phone number, email, and physical address.

Include a map or interactive location feature (if applicable).

Add social media links for easier customer engagement.

About Us Page:

An engaging overview of the company’s history, values, and mission.

Highlight Tormique’s commitment to innovation and its role in the insurance market.

Include key team members with photos and bios to humanise the brand.

Detail Tormique’s vision and how it is revolutionising the insurance industry with technology and customer service.

Affiliate Page:

Dedicated to promoting the Tormique Affiliate Program.

Provide an overview of how the affiliate program works and how potential affiliates can get started.

Include details about the revenue share structure, benefits for affiliates, and the support they will receive.

Provide a sign-up form or CTA button for interested affiliates to join the program.

Include a FAQ section to answer common questions and clear up any confusion.

Product Page for Fleet Insurance:

A dedicated page for Motor Fleet Insurance detailing the unique aspects of this product.

Clearly explain the benefits of fleet insurance, how it works, and the types of businesses it covers.

Offer features such as flexible coverage options, real-time quotes via the auction process, and tailored pricing for fleet owners.

Include testimonials or case studies from businesses that have used Tormique’s fleet insurance service.

A prominent CTA button to encourage visitors to start an auction or get in touch for more details.

Additional Pages to Consider:

FAQs Page:

Address common questions regarding Tormique's services, products, and processes.

This could include queries about how the auction system works, how to get quotes, payment options, and policy details.

Testimonials Page:

Showcase customer feedback, case studies, and success stories.

Include both written testimonials and video content (if possible).

Partners Page:

Dedicated to potential business partners, highlighting opportunities to collaborate with Tormique, such as partnerships with brokers or other companies in the insurance ecosystem.

Offer a detailed breakdown of partnership benefits, requirements, and how to get started.

Resources Page:

A library of helpful content like blog articles, guides, industry reports, or white papers.

This page could also include downloadable resources like checklists, templates, or policy samples to help customers make informed decisions.

For any text area without text, you can add example text to fill the space.

*Images uploaded are only a guideline
If you have any questions, please let me know

Target Market(s)

B2B, software for quoting niche insurance products which can't be found on traditional comparison sites

Industry/Entity Type

Insurance / Insurtech / Software / Technology

Number of Pages Required

5+ page

Font styles to use
Other font styles liked:
• See: Project description for information

Requirements
Must have
• See: Project description
Nice to have
Should not have

```html
<!DOCTYPE html>
<html lang="en">
<head>
<meta charset="utf-8">
<title>Tormique — Get Insured Smarter. Faster.</title>
<link rel="stylesheet" href="https://fonts.googleapis.com/css2?family=Poppins:wght@400;500;600;700&display=swap">
<style>
:root{
  --navy:#042a3e;
  --green:#22c06b;
  --ink:#0d2233;
  --muted:#4a5560;
  --grey-bg:#efefef;
  --white:#ffffff;
  --line:#d7dadd;
}
*{box-sizing:border-box;margin:0;padding:0}
html,body{width:1200px;height:4187px;overflow:hidden}
body{font-family:"Poppins",sans-serif;color:var(--ink);background:var(--white);position:relative}
.abs{position:absolute}
.btn{position:absolute;display:flex;align-items:center;justify-content:center;border-radius:40px;font-weight:500;font-size:16px;color:var(--white);background:var(--green);text-decoration:none}

/* header + hero */
.hero{position:absolute;left:0;top:0;width:1200px;height:619px;background:linear-gradient(180deg,#03283c 0%,#042b40 60%,#03263a 100%);overflow:hidden}
.brand{position:absolute;display:flex;align-items:center;gap:8px;font-weight:600;color:var(--white);white-space:nowrap}
.brand .dot{width:26px;height:26px;border-radius:50%;background:var(--green)}
.nav a{position:absolute;top:40px;font-size:12px;color:var(--white);text-decoration:none;white-space:nowrap}
.nav a.active{color:var(--green)}
.hero-glow{left:70px;top:200px;width:280px;height:340px;border-radius:50%;background:radial-gradient(ellipse at center,rgba(34,192,107,.28) 0%,rgba(34,192,107,.08) 45%,rgba(4,42,62,0) 70%)}
.hero-streak{left:250px;top:240px;width:820px;height:90px;background:radial-gradient(ellipse at left center,rgba(120,200,230,.16),rgba(4,42,62,0) 70%)}
.hero h1{position:absolute;left:0;width:1200px;text-align:center;font-size:46px;font-weight:700;line-height:1.2;color:var(--white)}
.hero h1 .accent{color:var(--green)}
.hero .lead{position:absolute;left:0;top:316px;width:1200px;text-align:center;font-size:16px;color:var(--white)}
.btn-ghost{background:transparent;border:2px solid var(--white)}

/* advantage */
.advantage{position:absolute;left:0;top:619px;width:1200px;height:462px;background:var(--white)}
h2.section-title{position:absolute;left:0;width:1200px;text-align:center;font-size:30px;font-weight:600;color:var(--ink)}
.feature{position:absolute;width:220px;text-align:center}
.feature svg{display:block;margin:0 auto}
.feature h3{font-size:15px;font-weight:600;margin-top:22px;white-space:nowrap}
.feature p{font-size:11.5px;line-height:19px;color:var(--muted);margin-top:18px}

/* how it works */
.how{position:absolute;left:0;top:1081px;width:1200px;height:958px;background:var(--navy);overflow:hidden}
.how h2.section-title{color:var(--white)}
.how .intro{position:absolute;left:245px;top:111px;width:710px;text-align:center;font-size:11.5px;line-height:19px;color:var(--white)}
.step-line{position:absolute;top:251px;left:330px;width:545px;height:3px;background:var(--white)}
.step{position:absolute;top:220px;width:62px;height:62px;border-radius:50%;background:var(--white);color:var(--ink);font-weight:600;font-size:18px;display:flex;align-items:center;justify-content:center}
.step.current{background:var(--green);color:var(--white)}
.how-glow{left:420px;top:330px;width:360px;height:620px;border-radius:50%;background:radial-gradient(ellipse at center,rgba(60,140,170,.28),rgba(4,42,62,0) 70%)}
.phone-visual{position:absolute;left:463px;top:371px;width:249px;height:515px;border-radius:40px;background:linear-gradient(180deg,#f4f6f8 0%,#dde3e8 100%)}

/* products */
.products{position:absolute;left:0;top:2039px;width:1200px;height:569px;background:var(--grey-bg)}
.card{position:absolute;top:137px;width:231px;height:326px;background:var(--white);border-radius:8px;overflow:hidden;box-shadow:0 2px 8px rgba(0,0,0,.06)}
.card .media{height:141px;background:linear-gradient(160deg,#6f8f7a 0%,#1f8a4a 45%,#3aa865 70%,#8a9a88 100%)}
.card h3{position:absolute;left:0;top:163px;width:100%;text-align:center;font-size:15px;font-weight:600}
.card p{position:absolute;left:0;top:197px;width:100%;text-align:center;font-size:15px;color:var(--muted)}
.card .btn{left:47px;top:244px;width:137px;height:48px;font-size:15px}

/* testimonials */
.testimonials{position:absolute;left:0;top:2608px;width:1200px;height:436px;background:var(--white)}
.video{position:absolute;left:206px;top:122px;width:324px;height:224px;background:linear-gradient(120deg,#c9ced1 0%,#9aa3a8 45%,#6f7f8e 70%,#dfe3e5 100%)}
.play{position:absolute;left:123px;top:83px;width:58px;height:58px;border-radius:50%;background:var(--green);display:flex;align-items:center;justify-content:center}
.quote{position:absolute;left:566px;top:122px;width:370px;font-size:11.5px;line-height:19px;color:var(--ink)}
.author{position:absolute;left:567px;top:211px;font-size:15px;font-weight:600;color:var(--green)}
.role{position:absolute;left:568px;top:241px;font-size:11px;color:var(--muted)}

/* blog */
.blog{position:absolute;left:0;top:3044px;width:1200px;height:450px;background:var(--grey-bg)}
.blog h2{position:absolute;left:205px;top:50px;font-size:30px;font-weight:600}
.post-img{position:absolute}
.post-title{position:absolute;font-size:14.5px;font-weight:600;color:var(--green);line-height:19px}
.post-date{position:absolute;font-size:11px;color:var(--muted)}
.divider{position:absolute;left:623px;top:254px;width:366px;height:1px;background:var(--line)}

/* cta */
.cta{position:absolute;left:0;top:3494px;width:1200px;height:262px;background:var(--green)}
.cta h2{position:absolute;left:0;top:38px;width:1200px;text-align:center;font-size:30px;font-weight:600;color:var(--white)}
.cta p{position:absolute;left:400px;top:96px;width:400px;text-align:center;font-size:11.5px;line-height:19px;color:var(--white)}
.cta .btn{left:532px;top:156px;width:135px;height:48px;background:var(--navy);font-size:15px}

/* footer */
.footer{position:absolute;left:0;top:3756px;width:1200px;height:431px;background:var(--navy);color:var(--white)}
.social{position:absolute;top:106px;width:38px;height:38px;border-radius:50%;background:var(--white)}
.fcol{position:absolute;top:188px}
.fcol h4{font-size:15px;font-weight:600;margin-bottom:20px}
.fcol li{list-style:none;font-size:11px;line-height:19px;white-space:nowrap}
.copy{position:absolute;left:206px;top:393px;font-size:11px}
</style>
</head>
<body>

<header class="hero">
  <div class="abs hero-glow" role="img" aria-label="Glowing green shield emblem decoration"></div>
  <div class="abs hero-streak"></div>
  <div class="brand" style="left:208px;top:34px;font-size:24px"><span class="dot"></span>Tormique</div>
  <nav class="nav">
    <a class="active" href="#" style="left:369px">Home</a>
    <a href="#" style="left:437px">How it works</a>
    <a href="#" style="left:543px">Products</a>
    <a href="#" style="left:629px">FAQs</a>
    <a href="#" style="left:693px">About</a>
    <a href="#" style="left:784px">Choose Product</a>
  </nav>
  <a class="btn" style="left:883px;top:28px;width:107px;height:42px;font-size:12px">Login</a>
  <h1 style="top:172px">Get Insured Smarter. Faster.</h1>
  <h1 style="top:227px"><span class="accent">On Your Terms.</span></h1>
  <p class="lead">AI-powered quotes. Real-time auctions. No broker spam.</p>
  <a class="btn" style="left:327px;top:395px;width:260px;height:63px">Start Comparing Quotes</a>
  <a class="btn btn-ghost" style="left:610px;top:395px;width:177px;height:63px">How It Works</a>
</header>

<section class="advantage">
  <h2 class="section-title" style="top:46px">Tormique Advantage</h2>
  <div class="feature" style="left:202px;top:124px">
    <svg width="38" height="38" viewBox="0 0 24 24" fill="none" stroke="#22c06b" stroke-width="1.6" stroke-linejoin="round" stroke-linecap="round"><path d="M14 3l7 7-3 3-7-7z"/><path d="M12.5 8.5L5 16a2.1 2.1 0 003 3l7.5-7.5"/><path d="M3 21h9"/></svg>
    <h3>Real-Time Auction Quotes</h3>
    <p>Get competitive rates through live insurer bidding — a smarter way to save on niche coverage.</p>
  </div>
  <div class="feature" style="left:490px;top:124px">
    <svg width="38" height="38" viewBox="0 0 24 24" fill="none" stroke="#22c06b" stroke-width="1.6" stroke-linecap="round"><circle cx="12" cy="12" r="9"/><circle cx="12" cy="12" r="5"/><path d="M12 12l7-7M16 5h3v3"/></svg>
    <h3>Tailored for Niche Markets</h3>
    <p>Motor trade? Unique fleet? Tormique specializes in hard-to-find insurance solutions built for you.</p>
  </div>
  <div class="feature" style="left:776px;top:124px">
    <svg width="38" height="38" viewBox="0 0 24 24" fill="none" stroke="#22c06b" stroke-width="1.6" stroke-linejoin="round"><path d="M13 2L4 14h7l-1 8 9-12h-7z"/></svg>
    <h3>AI-Powered Speed</h3>
    <p>Our AI understands your needs and delivers relevant quotes faster than ever.</p>
  </div>
  <a class="btn" style="left:532px;top:331px;width:154px;height:60px">Get Started</a>
</section>

<section class="how">
  <div class="abs how-glow"></div>
  <h2 class="section-title" style="top:48px">How it works</h2>
  <p class="intro">Share your insurance requirements once, and we'll notify our panel of partners through a virtual auction. They will carefully review your needs and respond with indicative pricing and policy features via the Tormique platform. When you're ready, you can select the partner you'd like to connect with at a time that best suits you to finalise your policy.</p>
  <div class="step-line"></div>
  <div class="step current" style="left:296px">1</div>
  <div class="step" style="left:484px">2</div>
  <div class="step" style="left:658px">3</div>
  <div class="step" style="left:841px">4</div>
  <div class="phone-visual" role="img" aria-label="Smartphone mockup showing the Tormique sign-up screen"></div>
</section>

<section class="products">
  <h2 class="section-title" style="top:46px">What products are available?</h2>
  <div class="card" style="left:208px">
    <div class="media" role="img" aria-label="Small group of green branded vans parked in a city street"></div>
    <h3>Small fleet insurance</h3><p>Upto 5 vehicles</p>
    <a class="btn">Get Started</a>
  </div>
  <div class="card" style="left:485px">
    <div class="media" role="img" aria-label="Row of green branded vans parked along a tree-lined road"></div>
    <h3>Medium fleet insurance</h3><p>Between 6 – 10 vehicles</p>
    <a class="btn">Get Started</a>
  </div>
  <div class="card" style="left:759px">
    <div class="media" role="img" aria-label="Large car park filled with many green branded vans"></div>
    <h3>Large fleet insurance</h3><p>More than 10 vehicles</p>
    <a class="btn">Get Started</a>
  </div>
</section>

<section class="testimonials">
  <h2 class="section-title" style="top:40px">Happy customers</h2>
  <div class="video" role="img" aria-label="Video testimonial of a business owner speaking in an office">
    <div class="play"><svg width="22" height="24" viewBox="0 0 22 24"><path d="M3 2l17 10-17 10z" fill="#fff"/></svg></div>
  </div>
  <p class="quote">“It was so easy! secured fleet cover for our 7 vehicles. very easy process, and it's very reassuring to know I wasn't going to be bombarded with multiple brokers' calls; only the one I selected called me and set my policy up at the price provided.”</p>
  <div class="author">Neil Ashcombe</div>
  <div class="role">CEO - Ravensmoor Packaging</div>
  <svg class="abs" style="left:572px;top:295px" width="70" height="30" viewBox="0 0 70 30" fill="none" stroke="#0d2233" stroke-width="2.2" stroke-linecap="round" stroke-linejoin="round"><path d="M16 3L5 15l11 12"/><path d="M54 3l11 12-11 12"/></svg>
</section>

<section class="blog">
  <h2>Recent blog</h2>
  <div class="post-img" style="left:206px;top:112px;width:384px;height:195px;background:linear-gradient(110deg,#5f7a66 0%,#2e4a3c 35%,#8aa1ad 65%,#d6dde2 100%)" role="img" aria-label="Stressed man reading insurance paperwork"></div>
  <div class="post-title" style="left:206px;top:328px;width:330px">Why Traditional Insurance Comparison Sites Don't Work for Niche Products</div>
  <div class="post-date" style="left:206px;top:372px">05 Apr 2025</div>

  <div class="post-img" style="left:623px;top:112px;width:125px;height:109px;background:linear-gradient(135deg,#1d3b63 0%,#b2343b 50%,#c9d6e6 100%)" role="img" aria-label="Digital brain visualisation representing AI"></div>
  <div class="post-title" style="left:761px;top:118px;width:230px">How AI is Transforming the Way Businesses Buy Insurance</div>
  <div class="post-date" style="left:761px;top:180px">05 Apr 2025</div>
  <div class="divider"></div>
  <div class="post-img" style="left:623px;top:278px;width:125px;height:109px;background:linear-gradient(135deg,#e8eaec 0%,#9aa4ad 50%,#4a5a6a 100%)" role="img" aria-label="Person working at computer screens in an office"></div>
  <div class="post-title" style="left:761px;top:284px;width:230px">7 Reasons Businesses Are Switching to Digital-First Insurance</div>
  <div class="post-date" style="left:761px;top:346px">05 Apr 2025</div>
</section>

<section class="cta">
  <h2>Get started today</h2>
  <p>It's safe, secure, hassle-free and costs nothing. Get started by creating a free account today.</p>
  <a class="btn">Get A Quote</a>
</section>

<footer class="footer">
  <div class="brand" style="left:536px;top:42px;font-size:24px"><span class="dot"></span>Tormique</div>
  <span class="social" style="left:509px"></span>
  <span class="social" style="left:556px"></span>
  <span class="social" style="left:605px"></span>
  <span class="social" style="left:651px"></span>
  <div class="fcol" style="left:206px">
    <h4>Contact</h4>
    <ul><li>support@tormique.example</li><li>&nbsp;</li><li>Fenwick House, 14 Larch Row, Ledbury,</li><li>Herefordshire,</li><li>United Kingdom,</li><li>HR8 1QZ</li></ul>
  </div>
  <div class="fcol" style="left:507px">
    <h4>Company</h4>
    <ul><li>About Us</li><li>Careers</li><li>Contact</li><li>Blog / News</li></ul>
  </div>
  <div class="fcol" style="left:688px">
    <h4>Product</h4>
    <ul><li>How It Works</li><li>Live Products</li><li>Coming Soon</li><li>Request a Quote</li></ul>
  </div>
  <div class="fcol" style="left:881px">
    <h4>Support</h4>
    <ul><li>Help Center</li><li>FAQs</li><li>Privacy Policy</li><li>Terms &amp; Conditions</li></ul>
  </div>
  <p class="copy">© 2025 Tormique Ltd. All rights reserved. | Registered in the UK | Powered by Innovation</p>
</footer>

</body>
</html>
```